Banner for home page on event planning site

We are revamping the home page www.coralbellecelebrations.com and would like to add a banner to the center of it to guide potential clients to one of 3 areas of the site:

Weddings, Corporate Events, Parties and More

I'm uploading an attachment that shows where the banner will be placed. It needs to have those 3 distinct sections, and match the existing colors/branding of the site. The fonts used for the logo are Lucida Bright and Callie Hand. Both are available for free.

Please use lorem ipsum under each section, I'll fill that in later. It should just be highly designed, beautiful, and easy to understand that clicking these will take you to the different areas of the site.
Updates

Hi designers,
Here are some problems we are having with the designs that have been submitted.
1) 3 stock images as squares... when you do this and then put it into the existing website, it gets lost among the other boxes. We need this to be where the eye goes immediately when you land on the site.
2) Not enough of a frame or white space... we think you need some white space to make this stand out as different from the surrounding area.
3) No clearly defined areas. It needs to be easy for people to figure out... Weddings, click here. Parties, click here. Corporate events, click here.

Industry/Entity Type

Event Planning

Requirements
Should not have
• Nothing with orchids, her competitor uses them and they are common in the event planning industry. We want to stay away from them.

Files

```html
<!DOCTYPE html>
<html lang="en">
<head>
<meta charset="utf-8">
<title>Coral Belle Celebrations – Event Banner</title>
<link rel="stylesheet" href="https://fonts.googleapis.com/css2?family=Libre+Baskerville&display=swap">
<style>
  :root {
    --wood-dark: #4a3219;
    --wood-mid: #6b4a2a;
    --wood-light: #7d5a34;
    --floor-dark: #6a3d22;
    --floor-light: #9a623c;
    --sky-top: #8ec8ea;
    --sky-low: #d6ecf6;
    --tree: #3f6b2e;
    --grass: #5fa02f;
    --pink: #c24f9e;
    --pink-light: #d972bb;
    --pink-dark: #9b3682;
    --pink-fold: #7a2766;
    --label: #ffffff;
  }
  * { box-sizing: border-box; margin: 0; padding: 0; }
  html, body { width: 1200px; height: 346px; overflow: hidden; }
  body { position: relative; }

  .wood-backdrop {
    position: absolute; inset: 0;
    background: linear-gradient(90deg, var(--wood-dark), var(--wood-mid) 30%, var(--wood-light) 55%, var(--wood-mid) 80%, var(--wood-dark));
  }

  .banner {
    position: absolute; left: 43px; top: 43px; width: 1115px; height: 261px;
    box-shadow: 0 4px 10px rgba(0,0,0,.55);
    overflow: hidden;
  }
  .banner__scenery {
    position: absolute; left: 0; top: 0; width: 100%; height: 204px;
    background: linear-gradient(180deg, var(--sky-top) 0%, var(--sky-low) 45%, var(--tree) 70%, var(--tree) 92%, var(--grass) 100%);
  }
  .banner__floor {
    position: absolute; left: 0; top: 204px; width: 100%; height: 57px;
    background: linear-gradient(180deg, var(--floor-light), var(--floor-dark));
  }

  .event-photo {
    position: absolute; width: 218px; height: 218px; border-radius: 50%;
    border: 5px solid var(--pink);
    box-shadow: 0 0 0 1px var(--pink-dark);
  }
  .event-photo--corporate { left: 127px; top: 41px; background: radial-gradient(circle at 45% 45%, #e6d7a8, #4a4a58 60%, #1f2230); }
  .event-photo--weddings  { left: 490px; top: 41px; background: radial-gradient(circle at 50% 45%, #f2ddc4, #d8c98a 55%, #9aa35a); }
  .event-photo--parties   { left: 856px; top: 41px; background: radial-gradient(circle at 50% 55%, #c98a4e, #8a4a2e 55%, #3d2418); }

  .section-ribbon { position: absolute; top: 189px; width: 336px; height: 56px; }
  .section-ribbon--corporate { left: 24px; }
  .section-ribbon--weddings  { left: 390px; }
  .section-ribbon--parties   { left: 753px; }
  .section-ribbon svg { position: absolute; inset: 0; }
  .section-ribbon__label {
    position: absolute; left: 36px; top: 6px; width: 264px; height: 44px;
    display: flex; align-items: center; justify-content: center;
    font-family: "Libre Baskerville", serif;
    font-variant: small-caps;
    font-size: 30px; letter-spacing: .5px;
    color: var(--label);
    text-shadow: 0 1px 2px rgba(80,20,60,.6);
    text-decoration: none;
  }
  .section-ribbon--corporate .section-ribbon__label { font-size: 26px; }
</style>
</head>
<body>
  <div class="wood-backdrop" role="img" aria-label="Wooden plank wall background"></div>

  <section class="banner">
    <div class="banner__scenery" role="img" aria-label="Landscape of blue sky, tree line and green lawn"></div>
    <div class="banner__floor" role="img" aria-label="Polished wooden floor"></div>

    <div class="event-photo event-photo--corporate" role="img" aria-label="Photo of hands raising champagne glasses in a toast"></div>
    <div class="event-photo event-photo--weddings" role="img" aria-label="Photo of a smiling bride and groom with a bouquet"></div>
    <div class="event-photo event-photo--parties" role="img" aria-label="Photo of guests dancing at a party in a hall"></div>

    <a class="section-ribbon section-ribbon--corporate" href="#corporate-events">
      <svg viewBox="0 0 336 56" width="336" height="56" aria-hidden="true">
        <defs>
          <linearGradient id="band" x1="0" y1="0" x2="0" y2="1">
            <stop offset="0" stop-color="#d972bb"/><stop offset="1" stop-color="#a83d8a"/>
          </linearGradient>
        </defs>
        <polygon points="0,2 44,0 44,40 0,43 12,22" fill="#b8489a"/>
        <polygon points="336,2 292,0 292,40 336,43 324,22" fill="#b8489a"/>
        <polygon points="36,44 44,40 44,50" fill="#7a2766"/>
        <polygon points="300,44 292,40 292,50" fill="#7a2766"/>
        <rect x="36" y="6" width="264" height="44" fill="url(#band)" stroke="#9b3682"/>
      </svg>
      <span class="section-ribbon__label">Corporate Events</span>
    </a>

    <a class="section-ribbon section-ribbon--weddings" href="#weddings">
      <svg viewBox="0 0 336 56" width="336" height="56" aria-hidden="true">
        <polygon points="0,2 44,0 44,40 0,43 12,22" fill="#b8489a"/>
        <polygon points="336,2 292,0 292,40 336,43 324,22" fill="#b8489a"/>
        <polygon points="36,44 44,40 44,50" fill="#7a2766"/>
        <polygon points="300,44 292,40 292,50" fill="#7a2766"/>
        <rect x="36" y="6" width="264" height="44" fill="url(#band)" stroke="#9b3682"/>
      </svg>
      <span class="section-ribbon__label">Weddings</span>
    </a>

    <a class="section-ribbon section-ribbon--parties" href="#parties">
      <svg viewBox="0 0 336 56" width="336" height="56" aria-hidden="true">
        <polygon points="0,2 44,0 44,40 0,43 12,22" fill="#b8489a"/>
        <polygon points="336,2 292,0 292,40 336,43 324,22" fill="#b8489a"/>
        <polygon points="36,44 44,40 44,50" fill="#7a2766"/>
        <polygon points="300,44 292,40 292,50" fill="#7a2766"/>
        <rect x="36" y="6" width="264" height="44" fill="url(#band)" stroke="#9b3682"/>
      </svg>
      <span class="section-ribbon__label">Parties</span>
    </a>
  </section>
</body>
</html>
```